Need Business Card for our Indian Grocery Store

Industry/Entity Type

Grocery Store

Contact Information for Business Card

Manoj Baweja
Director

Store Locations:

Larkfield
482 Elm Parade
P: 03 9172 5843

Ashvale
613 Carlow Road
P: 03 9238 6014

email: kvtmarts@mailnest.example

Requirements
Must have
• Our logo Colours

```html
<!DOCTYPE html>
<html lang="en">
<head>
<meta charset="utf-8">
<title>KVT Marts – Business Card</title>
<link href="https://fonts.googleapis.com/css2?family=Lato:wght@400;700&family=Saira:wght@700&display=swap" rel="stylesheet">
<style>
  :root {
    --brand-red: #e01a1f;
    --card-light: #ededed;
    --card-dark: #2a2728;
    --ink: #262626;
    --rule: #a9a9a9;
    --backdrop: #d6d6d6;
  }
  * { box-sizing: border-box; margin: 0; padding: 0; }
  html, body {
    width: 1200px; height: 896px; overflow: hidden;
    background: var(--backdrop);
  }
  .canvas {
    width: 1200px; height: 896px;
    display: flex; flex-direction: column;
    align-items: center; justify-content: center; gap: 40px;
  }
  .card {
    width: 600px; height: 367px;
    position: relative;
    box-shadow: 0 6px 18px rgba(0,0,0,0.18);
  }
  .card--front { background: var(--card-light); }
  .card--back {
    background: var(--card-dark);
    display: flex; align-items: center; justify-content: center;
  }
  .brand-name {
    font-family: "Saira", sans-serif;
    font-weight: 700;
    color: var(--brand-red);
    text-transform: uppercase;
    line-height: 1;
    white-space: nowrap;
  }
  .logo-block {
    position: absolute; left: 30px; top: 140px; width: 240px;
    text-align: center;
  }
  .logo-block .brand-name { font-size: 38px; letter-spacing: 1px; }
  .tagline {
    margin-top: 14px;
    display: flex; align-items: center; gap: 8px;
    font-family: "Lato", sans-serif;
    font-size: 12px; color: var(--brand-red);
    white-space: nowrap;
  }
  .tagline::before, .tagline::after {
    content: ""; flex: 1; height: 1px; background: var(--brand-red);
  }
  .divider {
    position: absolute; left: 292px; top: 104px;
    width: 1px; height: 160px; background: var(--rule);
  }
  .contact {
    position: absolute; left: 316px; top: 104px;
    font-family: "Lato", sans-serif; font-size: 15px;
    color: var(--ink); line-height: 1.32;
    white-space: nowrap;
  }
  .contact__name {
    font-family: "Saira", sans-serif; font-weight: 700;
    font-size: 21px; color: var(--brand-red);
    text-transform: uppercase; letter-spacing: 0.5px; line-height: 1.1;
  }
  .contact__role { font-size: 17px; margin-bottom: 2px; }
  .contact__store { color: var(--brand-red); text-transform: uppercase; letter-spacing: 0.3px; }
  .label { color: var(--brand-red); }
  .card--back .brand-name { font-size: 72px; letter-spacing: 4px; }
</style>
</head>
<body>
  <main class="canvas">
    <section class="card card--front">
      <div class="logo-block">
        <div class="brand-name">KVT Marts</div>
        <div class="tagline">Fresh Stock Every Day</div>
      </div>
      <div class="divider"></div>
      <div class="contact">
        <div class="contact__name">Manoj Baweja</div>
        <div class="contact__role">Director</div>
        <div class="contact__store">Larkfield</div>
        <div>482 Elm Parade | <span class="label">P:</span> 03 9172 5843</div>
        <div class="contact__store">Ashvale</div>
        <div>613 Carlow Road | <span class="label">P:</span> 03 9238 6014</div>
        <div><span class="label">E:</span> kvtmarts@mailnest.example</div>
      </div>
    </section>
    <section class="card card--back">
      <div class="brand-name">KVT Marts</div>
    </section>
  </main>
</body>
</html>
```